Banner Ad Needed For Real Estate Lending Firm

We are taking out a banner ad on one of the most highly trafficked real estate websites in New York. The ad will be 970x250. Display format will be JPEG or animated GIF, but original art files will be required as well from the winning designer.

Harbor Ridge Lending (or HRL) is one of the largest "hard money lenders" for real estate investors on the East Coast of the US. We lend for the following real estate investments: 1) Fix And Flip 2) New Construction 3) Cash Out Refinance. We close in 2-10 days. More information can be found on our website here: http://www.hrl7-example.net/

Our goal is to help small business owners, real estate investors, and commercial contractors quickly and efficiently finance their business activities. Our local hard money loan programs are tailored to your unique project needs. We fund fix and flip, new construction, and cash out refinance projects for non-owner occupied properties.

Target Market(s)

Real Estate Agents, Real Estate Investors, Mortgage Brokers, Other Real Estate Professionals

Industry/Entity Type

Real Estate

Font styles to use
Sans Serif

Requirements
Must have
• Must incorporate the fact that we close deals very fast (2 - 10 days), finance the following these 2 main types of investments (Fix and Flip, New Construction), and mention that Brokers can make up to 2.5 Points.
• See attached style guide for basic colors and fonts.
Nice to have
• Animated GIF might be a great feature!

```html
<!DOCTYPE html>
<html lang="en">
<head>
<meta charset="utf-8">
<title>Harbor Ridge Lending – Banner</title>
<link href="https://fonts.googleapis.com/css2?family=Montserrat:wght@400;500;600;700;800&display=swap" rel="stylesheet">
<style>
  :root {
    --page: #fdfdfc;
    --teal-deep: #0b5363;
    --teal-bright: #1592aa;
    --orange: #e08a00;
    --white: #ffffff;
  }
  html, body {
    margin: 0;
    padding: 0;
    width: 1200px;
    height: 1000px;
    overflow: hidden;
    background: var(--page);
    font-family: "Montserrat", sans-serif;
  }
  .banner {
    position: absolute;
    left: 118px;
    top: 342px;
    width: 971px;
    height: 251px;
    background: var(--teal-deep);
    overflow: hidden;
    color: var(--white);
  }
  .banner-shapes {
    position: absolute;
    inset: 0;
  }
  .brand {
    position: absolute;
    left: 36px;
    top: 22px;
    display: flex;
    align-items: center;
    gap: 12px;
  }
  .brand-square {
    width: 54px;
    height: 54px;
    background: var(--white);
  }
  .brand-name {
    font-weight: 700;
    font-size: 15px;
    line-height: 19px;
    letter-spacing: 0.2px;
    text-transform: uppercase;
  }
  .intro {
    position: absolute;
    left: 37px;
    top: 103px;
    font-size: 11.6px;
    font-weight: 500;
    margin: 0;
    white-space: nowrap;
  }
  .programs {
    position: absolute;
    left: 37px;
    top: 140px;
    margin: 0;
    padding: 0;
    list-style: none;
    font-size: 17.5px;
    font-weight: 600;
    line-height: 24.5px;
  }
  .broker-note {
    position: absolute;
    left: 37px;
    top: 222px;
    margin: 0;
    font-size: 11.6px;
    font-weight: 600;
    white-space: nowrap;
  }
  .speed-box {
    position: absolute;
    left: 326px;
    top: 146px;
    width: 238px;
    height: 67px;
    background: var(--orange);
    border-radius: 2px;
  }
  .speed-lead {
    position: absolute;
    left: 16px;
    top: 16px;
    font-size: 12px;
    font-weight: 700;
    line-height: 20px;
  }
  .speed-bolt {
    position: absolute;
    left: 102px;
    top: -8px;
    width: 56px;
    height: 84px;
  }
  .speed-days {
    position: absolute;
    left: 154px;
    top: 2px;
    width: 68px;
    text-align: center;
    font-weight: 700;
    line-height: 1;
  }
  .speed-days .in { display: block; font-size: 15px; margin-top: 3px; }
  .speed-days .range { display: block; font-size: 28px; font-weight: 800; margin-top: 1px; }
  .speed-days .unit { display: block; font-size: 15px; margin-top: 1px; }
  .web-address {
    position: absolute;
    left: 328px;
    top: 219px;
    width: 236px;
    font-size: 15px;
    font-weight: 500;
    letter-spacing: 2.2px;
    white-space: nowrap;
  }
</style>
</head>
<body>
  <div class="banner">
    <svg class="banner-shapes" width="971" height="251" viewBox="0 0 971 251" xmlns="http://www.w3.org/2000/svg">
      <defs>
        <linearGradient id="city-sky" x1="0" y1="0" x2="0" y2="1">
          <stop offset="0" stop-color="#1f5fa6"/>
          <stop offset="0.55" stop-color="#4f8cc8"/>
          <stop offset="1" stop-color="#b9a894"/>
        </linearGradient>
      </defs>
      <polygon points="492,0 688,0 630,173" fill="var(--teal-bright)"/>
      <polygon points="688,0 971,0 971,251 692,251 630,173" fill="url(#city-sky)" role="img" aria-label="Photo of city skyscrapers and a construction crane against a blue sky"/>
    </svg>

    <div class="brand">
      <div class="brand-square"></div>
      <div class="brand-name">Harbor<br>Ridge<br>Lending LLC</div>
    </div>

    <p class="intro">We provide twelve-month, interest only bridge financing for the following programs:</p>

    <ol class="programs">
      <li>1. Fix And Flip</li>
      <li>2. New Construction</li>
      <li>3. Cash Out Refinance</li>
    </ol>

    <p class="broker-note">Brokers can make up to 2.5 points.</p>

    <div class="speed-box">
      <div class="speed-lead">We close the<br>deal very fast</div>
      <svg class="speed-bolt" viewBox="0 0 56 84" xmlns="http://www.w3.org/2000/svg">
        <polygon points="32,0 54,0 38,26 48,26 30,50 40,50 2,84 22,54 12,54 26,30 16,30" fill="var(--white)"/>
      </svg>
      <div class="speed-days">
        <span class="in">in</span>
        <span class="range">2-10</span>
        <span class="unit">days.</span>
      </div>
    </div>

    <div class="web-address">www.hrl7-example.net</div>
  </div>
</body>
</html>
```